TKR Advisory Business Cards

Hi there,

I'd like to make a simple new business card design with the logo we already have created for our business.

I need a double sided business card with our logo on the front side and the company and person's details on the back side.

I'd like it to be on a white background and no background so I can potentially use it with either white paper or put it on different coloured paper in accordance with our business colours.

Please use the logo images I have attached and also the fonts.

So Front side:
- Logo in centre of business card (use medium logo so there is a pretty decent border around it, so don't want to fill the whole card but to make it prominent).

Back Side.
- We need 3 different business cards with the different people's name on each.

ie.

Dorian Halvreck
Business Development Manager

m +61 437 206 518
e dorian@tkradvisory.com.au
w tkradvisory.com.au

- Also I'd like to put only the cog/power button logo in the top right hand corner of the card.
(You might need to chop the current logo in half as I don't have a seperate log just for this)
- Also I'd like some lines running on the top left hand corner diagonally, anything that will add to the design or some swirling lines that add some cool effect to the card.

Also I'd like to maybe put our ABN in the bottom right hand corner of the card in a smaller font.

I'd like to also talk to the designer if possible so I can get my idea across a bit better.

Thanks!

Regards,
Dorian

```html
<!DOCTYPE html>
<html lang="en">
<head>
<meta charset="utf-8">
<title>TKR Advisory – Business Card</title>
<link rel="stylesheet" href="https://fonts.googleapis.com/css2?family=Comfortaa:wght@700&display=swap">
<style>
  :root {
    --ink: #36434a;
    --paper: #ffffff;
    --accent-top: #fb9e0a;
    --accent-bottom: #f6e90f;
    --mark-dot: #f5a40c;
  }
  html, body {
    margin: 0;
    padding: 0;
    overflow: hidden;
    background: var(--paper);
  }
  .card {
    position: relative;
    width: 1200px;
    height: 741px;
    background: var(--paper);
    overflow: hidden;
    font-family: "Comfortaa", sans-serif;
    font-weight: 700;
    color: var(--ink);
  }
  .brand-decoration {
    position: absolute;
    top: 0;
    right: 0;
    width: 500px;
    height: 570px;
  }
  .brand {
    position: absolute;
    left: 54px;
    top: 78px;
    display: flex;
    align-items: center;
    gap: 12px;
    font-size: 24px;
    color: var(--ink);
  }
  .brand-dot {
    width: 30px;
    height: 30px;
    border-radius: 50%;
    background: var(--mark-dot);
  }
  .person {
    position: absolute;
    left: 97px;
    top: 236px;
    margin: 0;
  }
  .person-name {
    margin: 0;
    font-size: 33px;
    line-height: 1;
    font-weight: 700;
  }
  .person-role {
    margin: 18px 0 0;
    font-size: 37px;
    line-height: 1;
  }
  .contacts {
    position: absolute;
    left: 97px;
    top: 390px;
    margin: 0;
    display: grid;
    grid-template-columns: 78px auto;
    row-gap: 14px;
    font-size: 34px;
    line-height: 35px;
  }
  .contacts dt, .contacts dd { margin: 0; }
  .abn {
    position: absolute;
    left: 787px;
    top: 644px;
    margin: 0;
    font-size: 30px;
    line-height: 1;
  }
</style>
</head>
<body>
  <main class="card">
    <svg class="brand-decoration" viewBox="0 0 500 570" role="img" aria-label="Large brand mark decoration in orange to yellow gradient">
      <defs>
        <linearGradient id="accent-fade" x1="0" y1="0" x2="0" y2="1">
          <stop offset="0" stop-color="var(--accent-top)" style="stop-color:#fb9e0a"/>
          <stop offset="1" stop-color="var(--accent-bottom)" style="stop-color:#f6e90f"/>
        </linearGradient>
      </defs>
      <rect x="0" y="-60" width="560" height="625" rx="70" fill="url(#accent-fade)"/>
    </svg>

    <div class="brand">
      <span class="brand-dot"></span>
      <span class="brand-name">TKR Advisory</span>
    </div>

    <header class="person">
      <h1 class="person-name">Dorian Halvreck</h1>
      <p class="person-role">Business Development Manager</p>
    </header>

    <dl class="contacts">
      <dt>m</dt><dd>+61 437 206 518</dd>
      <dt>e</dt><dd>dorian@tkradvisory.com.au</dd>
      <dt>w</dt><dd>tkradvisory.com.au</dd>
    </dl>

    <p class="abn">ABN: 5872 1093 465</p>
  </main>
</body>
</html>
```